AUSTRALIA SUPPLEMENT - Protein label design - CREATIVE, FEMININE, UNIQUE

I need help with the design of what will be my line of supplements. (Protein, plant base, collagen , BCAAs, etc)
I'm starting off with protein isolate - with the flavours VANILLA, CHOCOLATE, BOYSENBERRY, HONEYCOMB.
I need help with the design of what the product will look like for my range.
(Great opportunity for further work)

Looking for a unique, elegant, stand out, feminine design, some slight sparkle or something that stands out on a shelf.
With symbols to represent what's in it, raised text. with some quirky cute things on it. (not sure what) Something that captured young womens eyes and easy to understand. things on it that appeals to women such as
LOW CALORIE, GREAT TASTING, GLUTEN FREE, 100 NATURAL, NATURALLY SWEETENED, HIGH PROTEIN.etc and whatever you can think of (open to ideas) but within KMO guidelines.

Mostly just after the look and creativity of what the front will look like. Don't have to worry about the back area.

My market will be for females aged 18-35

I have a activewear line called DORUMEN which will go with this. which I will attach the logo below amongst some other things that match my packaging. (again open to ideas)

I have attached a label of what one will look like( EXAMPLE).
. Among others that look nice But again I want to be different, unique to stand out. I don't want it to look like these. it's just the only ones I found online I liked that suit my market.

Feel free to ask any questions! :)
Updates

Extending time as I want this to be to be what will be on the shelves of many stores. I know that needs time to be able to do a quality job.

Target Market(s)

18-35

Industry/Entity Type

Supplement

Font styles to use
Serif
Script

Colors
f9d9e8
ffffff
fbd3d4
ecf7fb
e4daeb
cfeae6
eea4c8
fdfad7
f59195

Requirements
Must have
• Word - DORUMEN
PROTEIN ISOLATE
FLAVOUR
SYMBOLS

Looking for a unique, elegant, stand out, colour, feminine design, some slight sparkle or something that stands out on a shelf.

IT WILL BE ON A WHITE TUB or CLEAR - Perhaps detail on the lid
Nice to have
• Looking for a unique, elegant, stand out, colour, feminine design, some slight sparkle or something that stands out on a shelf. Something artsy.

will be on a white or clear tub with a white label background (possibly)
Should not have
• I don’t want it dark looking.
Something bright, vibrant, whites, pinks, sparkles (maybe) colours.

I don't want the word activewear on it.

```html
<!DOCTYPE html>
<html lang="en">
<head>
<meta charset="utf-8">
<title>DORUMEN Whey Sculpt – Label</title>
<link rel="stylesheet" href="https://fonts.googleapis.com/css2?family=Cinzel:wght@400;500&family=Oswald:wght@300&family=Montserrat:wght@400;600&display=swap">
<style>
  :root {
    --backdrop: #dcdcdc;
    --rose: #bd8592;
    --rose-text: #b9707f;
    --blush-edge: #f2c9d3;
    --white: #ffffff;
    --ink: #333333;
    --milk-pink: #f4bccb;
    --cream: #f3e6c6;
    --berry: #d8525b;
  }
  * { box-sizing: border-box; margin: 0; padding: 0; }
  html, body { width: 1200px; height: 900px; overflow: hidden; }
  body { background: var(--backdrop); font-family: "Montserrat", sans-serif; position: relative; }

  .label {
    position: absolute; left: 40px; top: 201px;
    width: 992px; height: 440px;
    transform: scale(1.129); transform-origin: 0 0;
    overflow: hidden; background: var(--rose);
  }
  .label__shapes { position: absolute; inset: 0; width: 992px; height: 440px; }

  .blurb {
    position: absolute; left: 19px; top: 31px; width: 206px;
    color: var(--white); font-size: 8.6px; line-height: 12.6px; text-align: justify;
  }

  .benefits { position: absolute; left: 19px; top: 122px; width: 70px; list-style: none; }
  .benefit { display: flex; flex-direction: column; align-items: center; margin-bottom: 14px; text-align: center; }
  .benefit__icon { width: 26px; height: 26px; margin-bottom: 4px; }
  .benefit__text {
    color: var(--white); font-family: "Cinzel", serif; font-size: 7.5px; line-height: 9px; letter-spacing: 0.6px;
  }

  .product-photo {
    position: absolute; left: 92px; top: 124px; width: 272px; height: 316px;
    background:
      radial-gradient(ellipse 30% 40% at 62% 45%, var(--milk-pink) 0 96%, transparent 100%),
      radial-gradient(ellipse 14% 11% at 28% 84%, var(--berry) 0 92%, transparent 100%),
      radial-gradient(ellipse 42% 22% at 50% 82%, var(--cream) 0 90%, transparent 100%);
  }

  .brand__dot {
    position: absolute; left: 466px; top: 52px; width: 62px; height: 62px;
    border: 2px solid var(--rose-text); border-radius: 50%;
  }
  .brand__name {
    position: absolute; top: 164px; left: 0; width: 994px; text-align: center;
    font-family: "Cinzel", serif; font-size: 35px; letter-spacing: 4px; color: var(--rose-text); line-height: 1;
  }
  .category {
    position: absolute; top: 212px; left: 0; width: 994px; text-align: center;
    font-family: "Cinzel", serif; font-size: 9px; letter-spacing: 3.5px; color: var(--rose-text);
  }
  .product-name {
    position: absolute; left: 0; width: 994px; text-align: center;
    font-family: "Cinzel", serif; font-weight: 500; color: var(--rose-text); line-height: 1;
    font-size: 48px;
  }
  .product-name--first { top: 254px; }
  .product-name--second { top: 309px; }
  .flavour {
    position: absolute; top: 366px; left: 0; width: 994px; text-align: center;
    font-family: "Oswald", sans-serif; font-weight: 300; font-size: 15px; color: var(--ink);
  }
  .rule { position: absolute; left: 392px; top: 406px; width: 202px; height: 5px; background: var(--rose-text); }
  .net-weight {
    position: absolute; left: 392px; top: 416px; width: 202px; height: 24px;
    background: var(--rose); color: var(--white); text-align: center;
    font-family: "Cinzel", serif; font-size: 14px; line-height: 26px; letter-spacing: 0.5px;
  }

  .facts { position: absolute; left: 781px; top: 36px; width: 178px; color: var(--white); font-size: 5px; line-height: 7.3px; }
  .facts__title { font-weight: 600; font-size: 5px; }
  .facts__serving { font-size: 5.6px; border-bottom: 1.5px solid var(--white); padding-bottom: 1px; margin-bottom: 1px; }
  .facts table { width: 100%; border-collapse: collapse; }
  .facts td { padding: 0; }
  .facts td.num { width: 46px; }
  .facts__main { border-bottom: 1.5px solid var(--white); margin-bottom: 6px; }
  .facts__main tr.head td { font-size: 4px; line-height: 5px; border-bottom: 1px solid var(--white); }
  .facts__cols { display: flex; gap: 5px; }
  .facts__col { flex: 1; }
  .facts__col h4 { font-size: 4px; font-weight: 600; border-bottom: 1px solid var(--white); }
  .facts__col td { font-size: 4.6px; line-height: 7.3px; border-bottom: 0.5px solid rgba(255,255,255,.6); }
  .facts__col td.num { width: 24px; }
  .facts__ingredients { margin-top: 10px; border-top: 1px solid var(--white); padding-top: 4px; font-size: 5.4px; line-height: 9px; }
</style>
</head>
<body>
  <div class="label">
    <svg class="label__shapes" viewBox="0 0 992 440" aria-hidden="true">
      <path d="M214,0 L772,0 C692,95 682,330 772,440 L300,440 C318,260 292,90 214,0 Z" fill="var(--white)"/>
      <path d="M200,0 C272,85 300,250 286,440 L300,440 C318,260 292,90 214,0 Z" fill="var(--blush-edge)"/>
      <path d="M772,0 C692,95 682,330 772,440 L780,440 C720,330 716,110 786,0 Z" fill="var(--blush-edge)"/>
      <path d="M786,0 L992,0 L992,440 L780,440 C720,330 716,110 786,0 Z" fill="var(--rose)"/>
    </svg>

    <p class="blurb">Lorem ipsum dolor sit amet, consectetuer adipiscing elit, sed diam nonummy nibh euismod tincidunt ut laoreet dolore magna aliquam erat volutpat. Ut wisi enim ad minim veniam, quis p ex ea commodo consequat. Duis autem vel eum iriure dolor in hendrerit in</p>

    <ul class="benefits">
      <li class="benefit">
        <svg class="benefit__icon" viewBox="0 0 26 26" aria-hidden="true"><circle cx="13" cy="13" r="12" fill="none" stroke="#fff" stroke-width="1.4"/><path d="M7.5 13.5l3.5 3.5 7.5-8" fill="none" stroke="#fff" stroke-width="1.8" stroke-linecap="round" stroke-linejoin="round"/></svg>
        <span class="benefit__text">HIGH<br>PROTEIN</span>
      </li>
      <li class="benefit">
        <svg class="benefit__icon" viewBox="0 0 26 26" aria-hidden="true"><circle cx="13" cy="13" r="12" fill="none" stroke="#fff" stroke-width="1.4"/><path d="M7.5 13.5l3.5 3.5 7.5-8" fill="none" stroke="#fff" stroke-width="1.8" stroke-linecap="round" stroke-linejoin="round"/></svg>
        <span class="benefit__text">GLUTEN<br>FREE</span>
      </li>
      <li class="benefit">
        <svg class="benefit__icon" viewBox="0 0 26 26" aria-hidden="true"><circle cx="13" cy="13" r="12" fill="none" stroke="#fff" stroke-width="1.4"/><path d="M7.5 13.5l3.5 3.5 7.5-8" fill="none" stroke="#fff" stroke-width="1.8" stroke-linecap="round" stroke-linejoin="round"/></svg>
        <span class="benefit__text">LOW<br>CALORIE</span>
      </li>
    </ul>

    <div class="product-photo" role="img" aria-label="Photo of a jar of pink strawberry shake with fresh strawberries and white chocolate pieces"></div>

    <span class="brand__dot"></span>
    <div class="brand__name">DORUMEN</div>
    <div class="category">PROTEIN ISOLATE</div>

    <div class="product-name product-name--first">WHEY</div>
    <div class="product-name product-name--second">SCULPT</div>
    <div class="flavour">STRAWBERRY WHITE CHOCOLATE</div>
    <div class="rule"></div>
    <div class="net-weight">NET WEIGH: 2.00 G</div>

    <div class="facts">
      <p class="facts__title">NUTRITION INFORMATION</p>
      <p class="facts__serving">Serving Size: 30g (1 scoop) Servings per Container: 30</p>
      <table class="facts__main">
        <tr class="head"><td></td><td class="num">Per Serve</td><td class="num">Per 100g</td></tr>
        <tr><td>Energy</td><td class="num">511kJ</td><td class="num">1702kJ</td></tr>
        <tr><td></td><td class="num">122Cal</td><td class="num">407Cal</td></tr>
        <tr><td>Protein</td><td class="num">23.4g</td><td class="num">78.0g</td></tr>
        <tr><td>Fat, total</td><td class="num">2.1g</td><td class="num">6.9g</td></tr>
        <tr><td>Saturated</td><td class="num">1.4g</td><td class="num">4.6g</td></tr>
        <tr><td>Carbohydrate, total</td><td class="num">2.3g</td><td class="num">7.5g</td></tr>
        <tr><td>&nbsp;– Sugars</td><td class="num">1.1g</td><td class="num">3.8g</td></tr>
      </table>
      <div class="facts__cols">
        <div class="facts__col">
          <h4>AMINO ACID PROFILE</h4>
          <table>
            <tr><td>PER 100G</td><td class="num"></td></tr>
            <tr><td>L-Leucine</td><td class="num">8.61</td></tr>
            <tr><td>L-Valine</td><td class="num">4.92</td></tr>
            <tr><td>L-Threonine</td><td class="num">4.9</td></tr>
            <tr><td>L-Phenylalanine</td><td class="num">2.79</td></tr>
            <tr><td>L-Arginine</td><td class="num">2.4</td></tr>
            <tr><td>L-Cysteine</td><td class="num">1.36</td></tr>
            <tr><td>L-Glutamic Acid</td><td class="num">15.93</td></tr>
            <tr><td>L-Histidine</td><td class="num">1.63</td></tr>
            <tr><td>L-Serine</td><td class="num">4.66</td></tr>
            <tr><td>L-Isoleucine</td><td class="num">5.19</td></tr>
            <tr><td>L-Lysine</td><td class="num">6.13</td></tr>
            <tr><td>L-Methionine</td><td class="num">1.84</td></tr>
            <tr><td>L-Tryptophan</td><td class="num">1.3</td></tr>
            <tr><td>L-Aspartic Acid</td><td class="num">7.18</td></tr>
            <tr><td>L-Alanine</td><td class="num">3.79</td></tr>
            <tr><td>L-Glycine</td><td class="num">1.66</td></tr>
            <tr><td>L-Proline</td><td class="num">2.88</td></tr>
            <tr><td>L-Tyrosine</td><td class="num">2.84</td></tr>
          </table>
        </div>
        <div class="facts__col">
          <h4>VITAMIN &amp; MINERAL BREAKDOWN</h4>
          <table>
            <tr><td>PER 30G</td><td class="num"></td></tr>
            <tr><td>Vit A</td><td class="num">2µg</td></tr>
            <tr><td>B1</td><td class="num">4µg</td></tr>
            <tr><td>B2</td><td class="num">5µg</td></tr>
            <tr><td>B3</td><td class="num">0.03mg</td></tr>
            <tr><td>Folate</td><td class="num">1µg</td></tr>
            <tr><td>B6</td><td class="num">5µg</td></tr>
            <tr><td>B12</td><td class="num">1µg</td></tr>
            <tr><td>C</td><td class="num">0.2mg</td></tr>
            <tr><td>D</td><td class="num">1µg</td></tr>
            <tr><td>E</td><td class="num">0.03mg</td></tr>
            <tr><td>Calcium</td><td class="num">3mg</td></tr>
            <tr><td>Iodine</td><td class="num">1µg</td></tr>
            <tr><td>Iron</td><td class="num">0.03mg</td></tr>
            <tr><td>Phosphorus</td><td class="num">3mg</td></tr>
            <tr><td>Zinc</td><td class="num">0.03mg</td></tr>
            <tr><td>Biotin</td><td class="num">1µg</td></tr>
            <tr><td>B5</td><td class="num">5µg</td></tr>
            <tr><td>K</td><td class="num">1µg</td></tr>
            <tr><td>Chromium</td><td class="num">1µg</td></tr>
            <tr><td>Copper</td><td class="num">3µg</td></tr>
            <tr><td>Magnesium</td><td class="num">5µg</td></tr>
            <tr><td>Selenium</td><td class="num">1µg</td></tr>
          </table>
        </div>
      </div>
      <p class="facts__ingredients">Ingredients: Whey Protein Concentrate, Whey Protein Isolate, Soy Lecithin, Digestive Enzymes, Ashwagandha, Chromium, Vit A, Vit B1, Vit B6, Vit B12, Vit C, Vit D, Vit E, Folate, Niacin, Selenium, Zinc, Sodium, Potassium, Calcium, Magnesium, Iron, Copper, Stevia, Flavour (Strawberry).</p>
    </div>
  </div>
</body>
</html>
```